Inviting A6 Flyer for Church membership

We need an A6 size flyer for the church. We are looking for something fresh, inviting and impactful. Church new logo and current flyer design attached.
Back text as follows:
We would love to have you join us as our SPECIAL GUEST this Sunday at 10am.
You can find us at Harvest Lantern Family Church, 17-19 Marlow Crest Road
(Behind Brivo), Thornbury Meadow Village,QX4 7LB
For more information or for a chat, please call us on 07700 900418 / 07700 900752 or email church@hlfcuk-mail.test
Target Market(s)
Church
Industry/Entity Type
Church
Colors
Designer to choose colors to be used in the design.
Requirements
Must have
- fresh, inviting and impactful.
- Chruch logo (attached)
Should not have
- Too much going on

```html
<!DOCTYPE html>
<html lang="en">
<head>
<meta charset="utf-8">
<title>Harvest Lantern Ministries – Guest Flyer</title>
<link rel="stylesheet" href="https://fonts.googleapis.com/css2?family=Cinzel:wght@400;700&family=Libre+Baskerville:wght@700&family=Raleway:wght@300&display=swap">
<style>
  :root {
    --board: #6b6b6b;
    --paper: #ffffff;
    --navy: #0f1338;
    --navy-deep: #0a0e2c;
    --guest-blue: #0a3566;
    --brand-red: #a32a18;
    --brand-blue: #2a6fb5;
    --tag-blue: #2f4f6e;
    --rule: #7d93a8;
    --accent-red: #ef3e1c;
    --accent-blue: #1e8fd6;
    --accent-orange: #ef4a24;
    --ink-light: #ffffff;
    --ornament: #f1e9df;
  }
  * { box-sizing: border-box; margin: 0; padding: 0; }
  html, body { width: 1200px; height: 871px; overflow: hidden; }
  body { background: var(--board); position: relative; font-family: "Cinzel", serif; }

  .flyer { position: absolute; top: 48px; width: 516px; height: 730px; overflow: hidden; background: var(--navy); }
  .flyer--front { left: 55px; }
  .flyer--back { left: 625px; }

  .header { position: absolute; left: 0; top: 0; width: 100%; height: 248px; background: var(--paper); }
  .ornament { position: absolute; top: 0; width: 120px; height: 200px; }
  .ornament--left { left: 0; background: radial-gradient(circle at 0 40%, var(--ornament), rgba(241,233,223,0) 70%); }
  .ornament--right { right: 0; background: radial-gradient(circle at 100% 40%, var(--ornament), rgba(241,233,223,0) 70%); }

  .brand-mark { position: absolute; left: 50%; top: 36px; width: 112px; height: 112px; margin-left: -56px; border-radius: 50%; background: var(--brand-blue); }
  .brand-name { position: absolute; left: 0; width: 100%; text-align: center; color: var(--brand-red); font-weight: 400; font-size: 27px; line-height: 1; }
  .brand-name--line1 { top: 145px; }
  .brand-name--line2 { top: 170px; }
  .brand-rule { position: absolute; left: 105px; width: 306px; top: 203px; height: 1px; background: var(--rule); }
  .tagline { position: absolute; left: 0; top: 207px; width: 100%; text-align: center; color: var(--tag-blue); font-size: 10.5px; line-height: 13px; letter-spacing: .2px; }

  .hero { position: absolute; left: 0; top: 248px; width: 100%; height: 482px;
    background: radial-gradient(ellipse at 45% 40%, #1a2046 0%, var(--navy) 55%, var(--navy-deep) 100%); }
  .guest-word { position: absolute; left: -6px; bottom: -30px; font-family: "Libre Baskerville", serif; font-weight: 700;
    font-size: 158px; line-height: 1; letter-spacing: -10px; color: var(--guest-blue); white-space: nowrap; }

  .invite { position: absolute; left: 0; top: 248px; width: 100%; height: 482px;
    background: radial-gradient(ellipse at 50% 30%, #141a44 0%, var(--navy) 60%, var(--navy-deep) 100%); }
  .line { position: absolute; left: 0; width: 100%; text-align: center; color: var(--ink-light); white-space: nowrap; line-height: 1; }
  .line--intro { font-size: 18px; }
  .line--special { font-size: 37px; color: var(--accent-red); }
  .line--venue { font-size: 24px; color: var(--accent-blue); }
  .line--address { font-size: 16.5px; }
  .line--phones { font-size: 24px; color: var(--accent-orange); }
  .line--phones span, .line--email span { color: var(--ink-light); }
  .line--email { font-size: 16px; }
  .line--email em { font-style: normal; font-size: 21px; color: var(--accent-orange); }

  .side-label { position: absolute; top: 810px; width: 516px; text-align: center; font-family: "Raleway", sans-serif;
    font-weight: 300; font-size: 32px; color: #ffffff; }
  .side-label--front { left: 55px; }
  .side-label--back { left: 625px; }
</style>
</head>
<body>

<section class="flyer flyer--front">
  <header class="header">
    <div class="ornament ornament--left" role="img" aria-label="Pale decorative mandala pattern"></div>
    <div class="ornament ornament--right" role="img" aria-label="Pale decorative mandala pattern"></div>
    <div class="brand-mark"></div>
    <p class="brand-name brand-name--line1">Harvest Lantern</p>
    <p class="brand-name brand-name--line2">Ministries</p>
    <div class="brand-rule"></div>
    <p class="tagline">Worshipping God, preaching the word<br>and doing the works of Jesus Christ.</p>
  </header>
  <div class="hero" role="img" aria-label="Dark photo of a cross silhouette against a cloudy night sky"></div>
  <p class="guest-word">GUEST</p>
</section>

<section class="flyer flyer--back">
  <header class="header">
    <div class="ornament ornament--left" role="img" aria-label="Pale decorative mandala pattern"></div>
    <div class="ornament ornament--right" role="img" aria-label="Pale decorative mandala pattern"></div>
    <div class="brand-mark"></div>
    <p class="brand-name brand-name--line1">Harvest Lantern</p>
    <p class="brand-name brand-name--line2">Ministries</p>
    <div class="brand-rule"></div>
    <p class="tagline">Worshipping God, preaching the word<br>and doing the works of Jesus Christ.</p>
  </header>
  <div class="invite">
    <p class="line line--intro" style="top:33px">We would love to</p>
    <p class="line line--intro" style="top:54px">have you join us as our</p>
    <p class="line line--special" style="top:76px">SPECIAL GUEST</p>
    <p class="line line--intro" style="top:114px">this Sunday at 10am.</p>
    <p class="line line--intro" style="top:163px">You can find us at</p>
    <p class="line line--venue" style="top:188px">Harvest Lantern</p>
    <p class="line line--venue" style="top:217px">Family Church</p>
    <p class="line line--address" style="top:252px">17-19 Marlow Crest Road(Behind Brivo),</p>
    <p class="line line--address" style="top:276px">Thornbury Meadow Village, QX4 7LB</p>
    <p class="line line--intro" style="top:336px">For more information or</p>
    <p class="line line--intro" style="top:357px">for a chat, please call us on</p>
    <p class="line line--phones" style="top:377px">07700 900418 / 07700 900752 <span style="font-size:18px">or</span></p>
    <p class="line line--email" style="top:406px">email <em>church@hlfcuk-mail.test</em></p>
  </div>
</section>

<p class="side-label side-label--front">FRONT</p>
<p class="side-label side-label--back">BACK</p>

</body>
</html>
```